Interior Design/ New Construction interior finishes

Interior Design Website

Target Market(s)

Home builders, New Construction, Renovations, Public

Industry/Entity Type

Construction

Coding

Coded - Design and coding required

Number of Pages Required

1 page

Font styles to use
Sans Serif

Colors

Designer to choose colors to be used in the design.

Requirements
Must have
• Section to upload pictures of projects
• Simple and modern design
• Designer 1 details about myself
• Logo
• Upload section for photos for future jobs
Nice to have
• Sections they can click on to see certain rooms in a house
• Decorating, floral arrangements, holiday decorating.
• I have lots of before and after as well. Maybe a section for those.

```html
<!DOCTYPE html>
<html lang="en">
<head>
<meta charset="utf-8">
<title>Alder Interiors — Interior Design</title>
<link rel="stylesheet" href="https://fonts.googleapis.com/css2?family=Raleway:wght@400;500;600;700&family=Open+Sans:wght@400;600;700;800&family=Montserrat:wght@400;500;600&display=swap">
<style>
  :root{
    --teal:#3a9ea8;
    --teal-dark:#2f8891;
    --ink:#1e1e1e;
    --white:#ffffff;
    --paper:#f3f3f3;
    --grey-text:#b9b9b9;
    --footer:#333333;
    --footer-line:#444444;
    --box:#e9e9e9;
  }
  *{box-sizing:border-box;margin:0;padding:0}
  html,body{width:1200px;height:3041px;overflow:hidden;background:var(--white)}
  body{font-family:"Raleway",Arial,sans-serif;color:var(--ink);position:relative}
  section,header,footer{position:absolute;left:0;width:1200px}

  /* Header */
  .site-header{top:0;height:126px;background:var(--white)}
  .nav{position:absolute;top:54px;display:flex;align-items:center;font-family:"Montserrat",sans-serif;font-size:12px;letter-spacing:.5px;text-transform:uppercase}
  .nav a{color:var(--ink);text-decoration:none}
  .nav .sep{display:inline-block;width:1px;height:14px;background:#555;margin:0 33px}
  .nav-left{left:133px}
  .nav-right{left:756px}
  .brand{position:absolute;left:0;width:1200px;top:12px;text-align:center}
  .brand-dot{display:block;width:62px;height:62px;border:2px solid var(--ink);border-radius:50%;margin:0 auto 6px}
  .brand-name{font-family:"Raleway",sans-serif;font-weight:500;font-size:21px;letter-spacing:2px;color:var(--ink)}

  /* Hero */
  .hero{top:126px;height:666px;background:linear-gradient(180deg,#6a625d 0%,#564d48 45%,#4a4441 100%)}
  .hero-photo{position:absolute;inset:0;background:linear-gradient(90deg,rgba(40,36,34,.55) 0%,rgba(120,110,102,.25) 50%,rgba(200,200,200,.2) 88%,rgba(60,55,52,.4) 100%)}
  .hero-tag{position:absolute;top:220px;width:100%;text-align:center;color:var(--white);font-family:"Raleway",sans-serif;font-weight:500;font-size:19px;letter-spacing:.5px;text-transform:uppercase}
  .hero-title{position:absolute;left:388px;top:272px;width:424px;height:86px;border:2px solid var(--teal);display:flex;align-items:center;justify-content:center;color:var(--white);font-family:"Raleway",sans-serif;font-weight:700;font-size:54px}
  .hero-actions{position:absolute;top:412px;left:0;width:100%;display:flex;justify-content:center;gap:16px}
  .btn{display:inline-flex;align-items:center;justify-content:center;width:134px;height:32px;font-family:"Montserrat",sans-serif;font-size:11px;font-weight:600;text-transform:uppercase;letter-spacing:.3px}
  .btn-teal{background:var(--teal);color:var(--white)}
  .btn-white{background:var(--white);color:var(--ink)}

  /* Services */
  .services{top:792px;height:424px;background:var(--white)}
  .service{position:absolute;top:80px;width:220px;text-align:center}
  .service svg{display:block;margin:0 auto}
  .service-label{margin-top:26px;font-family:"Montserrat",sans-serif;font-size:14px;letter-spacing:1px;text-transform:uppercase}

  /* About */
  .about{top:1216px;height:614px;background:linear-gradient(180deg,#4a4f52 0%,#3e4446 55%,#2f3a3b 100%)}
  .about-photo{position:absolute;inset:0;background:linear-gradient(180deg,rgba(0,0,0,.15),rgba(20,40,40,.35))}
  .section-title{position:absolute;width:100%;text-align:center;font-family:"Raleway",sans-serif;font-weight:700;font-size:34px}
  .section-title .accent{color:var(--teal)}
  .about .section-title{top:60px;color:var(--white)}
  .bracket{position:absolute;height:40px;border-top:2px solid currentColor}
  .bracket.left{border-left:2px solid currentColor}
  .bracket.right{border-right:2px solid currentColor}
  .about .bracket{color:#e6e6e6;top:82px}
  .about .bracket.left{left:132px;width:148px}
  .about .bracket.right{left:920px;width:148px}
  .logo-box{position:absolute;left:212px;top:170px;width:354px;height:322px;background:var(--box);display:flex;flex-direction:column;align-items:center;justify-content:center}
  .logo-box .brand-dot{width:100px;height:100px;border-width:3px;margin-bottom:14px}
  .logo-box .brand-name{font-size:34px;letter-spacing:3px}
  .kicker{position:absolute;left:620px;font-family:"Open Sans",sans-serif;font-weight:700;font-size:26px;text-transform:uppercase}
  .kicker .slash{color:var(--teal);margin-right:8px}
  .lede{position:absolute;left:620px;width:460px;font-family:"Open Sans",sans-serif;font-weight:800;font-size:30px;line-height:36px;text-transform:uppercase}
  .about .kicker{top:218px;color:var(--white)}
  .about .lede{top:290px;color:var(--white)}

  /* Projects */
  .projects{top:1830px;height:516px;background:var(--white)}
  .projects .section-title{top:82px;color:var(--ink)}
  .projects .bracket{color:var(--teal-dark);top:102px}
  .projects .bracket.left{left:132px;width:148px}
  .projects .bracket.right{left:920px;width:148px}
  .filter-panel{position:absolute;left:212px;top:186px;width:354px;height:330px;background:var(--teal)}
  .filters{position:absolute;right:32px;top:46px;list-style:none;text-align:right}
  .filters li{font-family:"Montserrat",sans-serif;font-weight:600;font-size:10px;color:var(--white);text-transform:uppercase;margin-bottom:26px;padding-bottom:3px;border-bottom:2px solid var(--white);display:table;margin-left:auto}
  .panel-actions{position:absolute;left:28px;top:248px;display:flex}
  .panel-actions .btn{height:26px;font-size:10px;width:130px}
  .btn-dark{background:#1f1f1f;color:var(--white);width:164px!important}
  .projects .kicker{top:236px;color:var(--ink)}
  .projects .lede{top:306px;color:var(--grey-text);width:420px}

  /* Photo strip */
  .photo-strip{top:2346px;height:250px;display:flex}
  .photo{height:250px}

  /* Signup */
  .signup{top:2596px;height:300px;background:var(--paper);text-align:center}
  .signup h2{position:absolute;top:82px;width:100%;font-family:"Raleway",sans-serif;font-weight:500;font-size:34px}
  .signup p{position:absolute;top:130px;width:100%;font-family:"Open Sans",sans-serif;font-size:12px;line-height:16px;color:#555}
  .signup-form{position:absolute;left:268px;top:196px;width:600px;height:32px;display:flex}
  .signup-input{flex:1;background:#e2e2e2;font-family:"Open Sans",sans-serif;font-style:italic;font-size:11px;color:#777;text-align:left;padding:9px 16px}
  .signup-btn{width:126px;background:var(--teal);color:var(--white);font-family:"Montserrat",sans-serif;font-weight:600;font-size:12px;text-transform:uppercase;display:flex;align-items:center;justify-content:center}

  /* Footer */
  .site-footer{top:2896px;height:145px;background:var(--footer)}
  .footer-brand{position:absolute;left:130px;top:16px;text-align:center}
  .footer-brand .brand-dot{width:60px;height:60px;border-color:var(--white);margin-bottom:6px}
  .footer-brand .brand-name{color:var(--white);font-size:19px;letter-spacing:2px}
  .footer-nav{position:absolute;left:330px;top:52px;display:flex;font-family:"Montserrat",sans-serif;font-size:10px;color:#ddd;text-transform:uppercase}
  .footer-nav span{margin-right:26px}
  .socials{position:absolute;left:906px;top:44px;display:flex;gap:6px}
  .socials span{width:28px;height:28px;background:#4a4a4a}
  .copyright{position:absolute;left:0;width:100%;bottom:0;height:28px;border-top:1px solid var(--footer-line);background:#2b2b2b;text-align:center;font-family:"Open Sans",sans-serif;font-size:10px;line-height:28px;color:#aaa}
</style>
</head>
<body>

<header class="site-header">
  <nav class="nav nav-left"><a>Home</a><span class="sep"></span><a>About Us</a><span class="sep"></span><a>Projects</a></nav>
  <div class="brand"><span class="brand-dot"></span><span class="brand-name">Alder Interiors</span></div>
  <nav class="nav nav-right"><a>Gallery</a><span class="sep"></span><a>Services</a><span class="sep"></span><a>Contact Us</a></nav>
</header>

<section class="hero">
  <div class="hero-photo" role="img" aria-label="Photo of a furnished master bedroom with tray ceiling, ceiling fan and upholstered bench"></div>
  <p class="hero-tag">Lorem ipsum dolor sit amet, consectetur adipiscing elit,</p>
  <h1 class="hero-title">Alder Interiors</h1>
  <div class="hero-actions"><span class="btn btn-teal">Our Projects</span><span class="btn btn-white">Get a Quote</span></div>
</section>

<section class="services">
  <div class="service" style="left:119px">
    <svg width="200" height="220" viewBox="0 0 200 220">
      <polygon points="100,8 192,60 192,160 100,212 8,160 8,60" fill="none" stroke="var(--teal)" stroke-width="2.5"/>
      <polygon points="100,22 196,196 4,196" fill="#8a7b6e" role="img" aria-label="Photo of a decorated room with built-in cabinetry"/>
    </svg>
    <p class="service-label">Decorating</p>
  </div>
  <div class="service" style="left:362px">
    <svg width="240" height="220" viewBox="0 0 240 220">
      <polygon points="110,8 202,60 202,160 110,212 18,160 18,60" fill="none" stroke="var(--teal)" stroke-width="2.5"/>
      <line x1="52" y1="14" x2="230" y2="116" stroke="#aaa" stroke-dasharray="3 3"/>
      <polygon points="56,20 232,116 56,212" fill="#b9b6b1" role="img" aria-label="Photo of a dining table with a floral centrepiece"/>
    </svg>
    <p class="service-label">Floral Arrangements</p>
  </div>
  <div class="service" style="left:620px">
    <svg width="220" height="220" viewBox="0 0 220 220">
      <polygon points="110,8 202,60 202,160 110,212 18,160 18,60" fill="none" stroke="var(--teal)" stroke-width="2.5"/>
      <polygon points="110,16 210,116 110,216 10,116" fill="#8a5a3c" role="img" aria-label="Photo of a living room decorated for the holidays"/>
    </svg>
    <p class="service-label">Holiday Decorating</p>
  </div>
  <div class="service" style="left:859px">
    <svg width="220" height="220" viewBox="0 0 220 220">
      <polygon points="110,8 202,60 202,160 110,212 18,160 18,60" fill="none" stroke="var(--teal)" stroke-width="2.5"/>
      <polygon points="6,30 204,30 105,200" fill="#9ea4a6" role="img" aria-label="Photo of a bright bathroom with freestanding tub"/>
    </svg>
    <p class="service-label">Interior Design</p>
  </div>
</section>

<section class="about">
  <div class="about-photo" role="img" aria-label="Photo of a brick home exterior with a pool at dusk"></div>
  <span class="bracket left"></span><span class="bracket right"></span>
  <h2 class="section-title">About <span class="accent">MySelf</span></h2>
  <div class="logo-box"><span class="brand-dot"></span><span class="brand-name">Alder Interiors</span></div>
  <h3 class="kicker"><span class="slash">/</span>About Myself</h3>
  <p class="lede">Lorem ipsum dolor sit amet, consectetu adipiscing elit, sed do eiusmod tempor incididunt ut labore</p>
</section>

<section class="projects">
  <span class="bracket left"></span><span class="bracket right"></span>
  <h2 class="section-title">Projects <span class="accent">Gallery</span></h2>
  <div class="filter-panel">
    <ul class="filters">
      <li>All</li><li>Decorating</li><li>Floral Arrangements</li><li>Holiday Decorating</li><li>Interior Architectural</li>
    </ul>
    <div class="panel-actions"><span class="btn btn-white">Upload Pictures</span><span class="btn btn-dark">Click On To See Rooms</span></div>
  </div>
  <h3 class="kicker"><span class="slash">/</span>Projects &amp; Gallery</h3>
  <p class="lede">Lorem ipsum dolor sit amet, consectetu adipiscing elit, sed do eiusmod tempor incididunt ut labore</p>
</section>

<section class="photo-strip">
  <div class="photo" style="width:314px;background:linear-gradient(135deg,#d8d8d6,#8e8e8c)" role="img" aria-label="Photo of a white kitchen with farmhouse sink"></div>
  <div class="photo" style="width:286px;background:linear-gradient(135deg,#a9a39a,#d6d2cb)" role="img" aria-label="Photo of a dining nook with upholstered chairs and flowers"></div>
  <div class="photo" style="width:284px;background:linear-gradient(135deg,#8c7565,#c3ab98)" role="img" aria-label="Photo of a bedroom with tufted headboard and bench"></div>
  <div class="photo" style="width:316px;background:linear-gradient(135deg,#c9ccd0,#9a9088)" role="img" aria-label="Photo of a living room with a rustic coffee table"></div>
</section>

<section class="signup">
  <h2>Don’t Forget To Sign Up!</h2>
  <p>Find out early about all upcoming promotions and new products releases<br>with our newsletter</p>
  <div class="signup-form"><span class="signup-input">Enter Your Email Address</span><span class="signup-btn">Subscribe</span></div>
</section>

<footer class="site-footer">
  <div class="footer-brand"><span class="brand-dot"></span><span class="brand-name">Alder Interiors</span></div>
  <nav class="footer-nav"><span>Home</span><span>About Us</span><span>Elements</span><span>Projects</span><span>Press</span><span>Videos</span><span>Services</span><span>Contact Us</span></nav>
  <div class="socials"><span></span><span></span><span></span><span></span><span></span></div>
  <p class="copyright">Copyright © 2018 Alder Interiors. All Rights Reserved.</p>
</footer>

</body>
</html>
```